Noche de Salsa

We need a poster to promote a party. It is a salsa night at La Tortuga, a fun night out to dance, be with friends and have a few drinks. It is an informal occasion. The drinks will not be expensive and the snack will be typical mexican food.
La Tortuga is a campus for 8 local non-profit organizations but it also has high quality event venues and outdoor areas.
We would like a file for print (11x17") and a digital file for social media.
Enclosed:
- File with poster contents in spanish.
- La Tortuga logo
- Picture of palm trees at La Tortuga (you don't have to include this if another graphic fits best.
- Pic of the outside of the restaurant, where the dancing will take place. The restaurante is right in fron of the beach. THIS PICTURE DOES NOT NECESSARILY NEEDS TO BE PART OF THE POSTER.
- La Tortuga Fact Sheet for context.
Target Market(s)
Men and women from 25 to 50 years old.
American and mexican citizens.
Industry/Entity Type
Non-Profit
Colors
Designer to choose colors to be used in the design.
Look and feel
Each slider illustrates characteristics of the customer's brand and the style your logo design should communicate.

```html
<!DOCTYPE html>
<html lang="es">
<head>
<meta charset="utf-8">
<title>Noche de Salsa · La Tortuga</title>
<link rel="stylesheet" href="https://fonts.googleapis.com/css2?family=Dancing+Script:wght@600&family=Open+Sans:wght@300;400;700&display=swap">
<style>
  :root {
    --night-blue: #2b4a98;
    --dusk-violet: #6d4fa3;
    --sunset-orange: #f07a3a;
    --salsa-pink: #e8265f;
    --sun-yellow: #f6c531;
    --script-yellow: #f5d84a;
    --date-cream: #f2e8a6;
    --palm-dark: #1a1d3c;
    --white: #ffffff;
  }
  * { margin: 0; padding: 0; box-sizing: border-box; }
  html, body { width: 777px; height: 1200px; overflow: hidden; background: var(--night-blue); }
  .poster {
    position: relative;
    width: 777px;
    height: 1200px;
    overflow: hidden;
    font-family: "Open Sans", Arial, sans-serif;
    color: var(--white);
    background:
      radial-gradient(ellipse 520px 520px at 85% 10%, var(--dusk-violet) 0%, rgba(109,79,163,0) 100%),
      linear-gradient(180deg, #30489a 0%, var(--night-blue) 60%, #2a3f8c 100%);
  }
  .dancer-illustration {
    position: absolute;
    left: 490px;
    top: 0;
    width: 287px;
    height: 1200px;
    background: linear-gradient(180deg, var(--sun-yellow) 0%, var(--sunset-orange) 30%, var(--salsa-pink) 45%, var(--sunset-orange) 65%, #f3a98a 100%);
    border-radius: 180px 0 0 120px;
    opacity: 0.92;
  }
  .palm-illustration {
    position: absolute;
    left: 380px;
    top: 590px;
    width: 130px;
    height: 300px;
    background: linear-gradient(180deg, rgba(26,29,60,0.85) 0%, rgba(26,29,60,0.55) 100%);
    border-radius: 50% 50% 10% 10%;
  }
  .brand {
    position: absolute;
    left: 38px;
    top: 28px;
    display: flex;
    align-items: center;
    gap: 12px;
  }
  .brand-dot { width: 30px; height: 30px; border-radius: 50%; background: var(--white); }
  .brand-name { font-size: 42px; font-weight: 400; color: var(--white); }
  .title {
    position: absolute;
    font-family: "Dancing Script", cursive;
    font-weight: 600;
    color: var(--script-yellow);
    line-height: 1;
  }
  .title-noche { left: 70px; top: 350px; font-size: 100px; }
  .title-salsa { left: 215px; top: 462px; font-size: 104px; }
  .date { position: absolute; left: 46px; top: 505px; color: var(--date-cream); font-weight: 300; line-height: 1.15; }
  .date-weekday { font-size: 36px; }
  .date-day { font-size: 64px; font-weight: 400; line-height: 1; margin: 4px 0 6px; }
  .date-month, .date-year { font-size: 38px; }
  .drinks-icon { position: absolute; left: 38px; top: 752px; width: 72px; height: 56px; }
  .entry { position: absolute; left: 40px; top: 828px; font-size: 32px; font-weight: 300; line-height: 1.3; }
  .venue { position: absolute; left: 40px; top: 950px; font-size: 19px; font-weight: 300; line-height: 1.4; font-style: normal; }
  .venue-name { font-size: 21px; font-weight: 400; margin-bottom: 2px; }
  .contact { position: absolute; left: 40px; top: 1138px; font-size: 19px; font-weight: 400; }
</style>
</head>
<body>
<main class="poster">
  <div class="dancer-illustration" role="img" aria-label="Ilustración de una mujer bailando salsa con sombrero y vestido rosa y naranja"></div>
  <div class="palm-illustration" role="img" aria-label="Silueta de palmera oscura"></div>

  <div class="brand">
    <span class="brand-dot"></span>
    <span class="brand-name">La Tortuga</span>
  </div>

  <h1 class="title title-noche">Noche de</h1>
  <p class="title title-salsa">Salsa!</p>

  <div class="date">
    <p class="date-weekday">Viernes</p>
    <p class="date-day">14</p>
    <p class="date-month">de Noviembre</p>
    <p class="date-year">2014</p>
  </div>

  <svg class="drinks-icon" viewBox="0 0 72 56" aria-hidden="true">
    <path d="M4 6 L26 6 L22 50 L8 50 Z" fill="#ffffff"/>
    <line x1="18" y1="0" x2="14" y2="14" stroke="#ffffff" stroke-width="3"/>
    <rect x="36" y="18" width="22" height="32" rx="3" fill="#ffffff"/>
    <path d="M58 24 h6 a4 4 0 0 1 4 4 v10 a4 4 0 0 1 -4 4 h-6" fill="none" stroke="#ffffff" stroke-width="4"/>
    <line x1="43" y1="24" x2="43" y2="44" stroke="#2b4a98" stroke-width="2"/>
    <line x1="51" y1="24" x2="51" y2="44" stroke="#2b4a98" stroke-width="2"/>
  </svg>

  <div class="entry">
    <p>Entrada: $100 pesos</p>
    <p>Incluye 1 bebida.</p>
  </div>

  <address class="venue">
    <p class="venue-name">La Tortuga</p>
    <p>Acceso Playa #1450</p>
    <p>(al final de la calle Palmas, junto al</p>
    <p>viejo muelle)</p>
    <p>Col. Las Brisas &nbsp;&nbsp;C.P. 23000 &nbsp;&nbsp;La Paz, B.C.S.</p>
  </address>

  <p class="contact">Más informes al 555-0148 / info@latortuga.org</p>
</main>
</body>
</html>
```